Larkfield Clinic Booklet 2016

Larkfield Clinic is a multi-specialty Practice in Midtown Manhattan offering advanced care in multiple areas of medicine. See our table of contents (PDF Uploaded)
Our designed booklet should be clean, easy to read, contemporary, high-end and elegant.
We need a general theme, Layout for cover and templates for internal.
We are entertaining the idea of two different sizes
8 x 10
or
11 x 8.5
Our tagline " The Future of Medicine is Here"
We will provide all the text content
The link to our website
www.LarkfieldCL.example
Uploaded files are as follows.. Logo, Our Team Photo and the PDF listing the table of contents.

```html
<!DOCTYPE html>
<html lang="en">
<head>
<meta charset="utf-8">
<title>Larkfield Clinic Booklet Cover</title>
<link rel="stylesheet" href="https://fonts.googleapis.com/css2?family=Roboto+Slab:wght@400;700&family=Raleway:wght@500&display=swap">
<style>
  :root {
    --backdrop: #9a9b9e;
    --navy-deep: #1f2440;
    --navy: #3a4066;
    --steel: #6b7598;
    --sky: #7fa3c8;
    --paper: #f4f4f6;
    --ink: #2a2d4a;
    --muted: #4a4d60;
    --photo-a: #9fb8d8;
    --photo-b: #d9dde4;
  }
  html, body {
    margin: 0;
    width: 1200px;
    height: 857px;
    overflow: hidden;
    background: var(--backdrop);
  }
  .spread {
    position: absolute;
    left: 120px;
    top: 118px;
    width: 960px;
    height: 620px;
    display: flex;
    box-shadow: 0 18px 40px rgba(0,0,0,.28);
  }
  .page {
    position: relative;
    width: 480px;
    height: 620px;
    background: var(--paper);
    overflow: hidden;
  }
  .page svg.backdrop-art { position: absolute; inset: 0; }
  .brand {
    position: absolute;
    display: flex;
    flex-direction: column;
    align-items: center;
    gap: 8px;
  }
  .brand-dot {
    width: 46px;
    height: 46px;
    border-radius: 50%;
    background: var(--navy);
  }
  .brand-name {
    font-family: "Roboto Slab", serif;
    font-weight: 400;
    font-size: 19px;
    line-height: 1.05;
    text-transform: uppercase;
    text-align: center;
    color: var(--ink);
    letter-spacing: .5px;
  }
  .web {
    position: absolute;
    font-family: "Raleway", sans-serif;
    font-weight: 500;
    font-size: 10px;
    letter-spacing: 3px;
    color: var(--muted);
  }
  .back-cover .brand { left: 200px; top: 330px; }
  .back-cover .web { left: 150px; top: 470px; }
  .team-photo {
    position: absolute;
    left: 40px;
    top: 20px;
    width: 400px;
    height: 300px;
    border-radius: 50%;
    background: linear-gradient(160deg, var(--photo-b), var(--photo-a));
    box-shadow: 8px 8px 0 var(--steel);
  }
  .front-cover .brand { left: 50px; top: 400px; }
  .tagline {
    position: absolute;
    left: 220px;
    top: 410px;
    font-family: "Roboto Slab", serif;
    color: var(--ink);
    margin: 0;
    font-size: 24px;
    line-height: 1.15;
  }
  .tagline strong { display: block; font-weight: 700; }
  .tagline span { display: block; font-weight: 400; font-size: 22px; }
  .front-cover .web { left: 222px; top: 485px; }
</style>
</head>
<body>
  <div class="spread">
    <section class="page back-cover">
      <svg class="backdrop-art" width="480" height="620" viewBox="0 0 480 620" aria-hidden="true">
        <defs>
          <linearGradient id="backNavy" x1="0" y1="0" x2="1" y2="1">
            <stop offset="0" stop-color="var(--navy-deep)"/>
            <stop offset="1" stop-color="var(--steel)"/>
          </linearGradient>
        </defs>
        <path d="M0,0 H480 V60 C300,110 90,330 0,600 Z" fill="var(--sky)"/>
        <path d="M0,0 H480 V40 C290,90 80,310 0,570 Z" fill="url(#backNavy)"/>
      </svg>
      <div class="brand">
        <div class="brand-dot"></div>
        <div class="brand-name">Larkfield<br>Clinic</div>
      </div>
      <div class="web">www.larkfieldcl.example</div>
    </section>
    <section class="page front-cover">
      <svg class="backdrop-art" width="480" height="620" viewBox="0 0 480 620" aria-hidden="true">
        <defs>
          <linearGradient id="frontNavy" x1="1" y1="0" x2="0" y2="1">
            <stop offset="0" stop-color="var(--navy-deep)"/>
            <stop offset="1" stop-color="var(--navy)"/>
          </linearGradient>
        </defs>
        <path d="M0,0 H480 V250 C320,250 150,300 0,380 Z" fill="url(#frontNavy)"/>
      </svg>
      <div class="team-photo" role="img" aria-label="Team photo of the clinic's doctors and nurses in scrubs and white coats"></div>
      <div class="brand">
        <div class="brand-dot"></div>
        <div class="brand-name">Larkfield<br>Clinic</div>
      </div>
      <h1 class="tagline"><strong>The Future of</strong><span>Medicine is Here</span></h1>
      <div class="web">www.larkfieldcl.example</div>
    </section>
  </div>
</body>
</html>
```